Business Card Design

I do estate sales and would like business card to reflect look and feel of attached logo. I also have copy of logo in .eps and .tif if you need that instead of .jpeg.
Updates

sorry for the delay in reviewing these designs. I will pick one by tomorrow. Here are the absolutes: *must have tagline (we find good homes for your treasures *must use blue and green *must be horizontal *nothing too fancy please submit your best and final. Thanks so much!

Industry/Entity Type

Business

Contact Information for Business Card

Mira Tolland

TAGS by MIRA
We find good homes for your treasures.

Specializing in one to three-day sales
o (no sale too big or too small)
• Home and garage organizing
• Home Clean-out

Call Mira Tolland at 202-555-0147
to schedule.

```html
<!DOCTYPE html>
<html lang="en">
<head>
<meta charset="utf-8">
<title>TAGS by MIRA — Business Card</title>
<link rel="stylesheet" href="https://fonts.googleapis.com/css2?family=Cinzel:wght@700&family=Questrial&display=swap">
<style>
  :root {
    --page-bg: #2a2a2a;
    --card-white: #ffffff;
    --green-light: #8ab04a;
    --green-mid: #6e9434;
    --green-dark: #4f6f22;
    --brand-green: #5f8a2c;
    --divider-blue: #1a7fa8;
    --ink-white: #ffffff;
    --ink-dark: #1b1f14;
  }
  * { margin: 0; padding: 0; box-sizing: border-box; }
  html, body {
    width: 1200px;
    height: 900px;
    overflow: hidden;
    background: var(--page-bg);
  }
  .business-card {
    position: absolute;
    left: 100px;
    top: 164px;
    width: 1000px;
    height: 572px;
    box-shadow: 0 18px 40px rgba(0,0,0,0.45);
  }
  .card-shapes {
    position: absolute;
    inset: 0;
    width: 100%;
    height: 100%;
  }
  .brand-panel {
    position: absolute;
    left: 0;
    top: 0;
    width: 310px;
    height: 572px;
    display: flex;
    align-items: center;
    justify-content: center;
    gap: 12px;
  }
  .brand-mark {
    width: 16px;
    height: 16px;
    background: var(--brand-green);
    flex: none;
  }
  .brand-name {
    font-family: "Questrial", sans-serif;
    font-weight: 400;
    font-size: 30px;
    letter-spacing: 1px;
    color: var(--brand-green);
    white-space: nowrap;
  }
  .info-panel {
    position: absolute;
    left: 360px;
    top: 0;
    width: 620px;
    height: 572px;
    color: var(--ink-white);
    text-align: center;
    font-family: "Questrial", sans-serif;
    padding-top: 58px;
  }
  .owner-name {
    font-family: "Cinzel", serif;
    font-weight: 700;
    font-size: 36px;
    letter-spacing: 5px;
  }
  .tagline {
    font-family: "Cinzel", serif;
    font-weight: 700;
    font-size: 22px;
    letter-spacing: 1px;
    line-height: 1.25;
    margin: 8px auto 0;
    width: 460px;
  }
  .services {
    list-style: none;
    margin-top: 44px;
    font-size: 24px;
    letter-spacing: 1.5px;
    line-height: 1.45;
  }
  .services li::before { content: "\2022\00a0"; }
  .services .note::before { content: none; }
  .call-block {
    margin-top: 40px;
    font-size: 22px;
    letter-spacing: 1.5px;
    line-height: 1.3;
  }
  .call-block .call-name {
    display: block;
    font-size: 32px;
    color: var(--ink-dark);
  }
  .call-block .phone {
    font-size: 30px;
    font-weight: 700;
    letter-spacing: 2px;
  }
  .call-block .small { font-size: 20px; opacity: 0.9; }
</style>
</head>
<body>
  <div class="business-card">
    <svg class="card-shapes" viewBox="0 0 1000 572" preserveAspectRatio="none" aria-hidden="true">
      <defs>
        <radialGradient id="greenGlow" cx="62%" cy="45%" r="70%">
          <stop offset="0" stop-color="#8ab04a"/>
          <stop offset="0.6" stop-color="#6e9434"/>
          <stop offset="1" stop-color="#4f6f22"/>
        </radialGradient>
      </defs>
      <rect x="0" y="0" width="1000" height="572" fill="#ffffff"/>
      <polygon points="300,0 1000,0 1000,572 340,572" fill="url(#greenGlow)"/>
      <line x1="300" y1="0" x2="340" y2="572" stroke="#1a7fa8" stroke-width="7"/>
    </svg>

    <div class="brand-panel">
      <span class="brand-mark" aria-hidden="true"></span>
      <p class="brand-name">TAGS by MIRA</p>
    </div>

    <div class="info-panel">
      <h1 class="owner-name">Mira Tolland</h1>
      <p class="tagline">We find good homes for your treasures</p>
      <ul class="services">
        <li>Specializing in one to three-day sales</li>
        <li class="note">(no sale too big or too small)</li>
        <li>Home and garage organizing</li>
        <li>Home Clean-out</li>
      </ul>
      <p class="call-block">
        Call
        <span class="call-name">Mira Tolland</span>
        <span class="small">at</span> <span class="phone">202-555-0147</span> <span class="small">to schedule</span>
      </p>
    </div>
  </div>
</body>
</html>
```